Business Card for mobile spray tan service
Mist Aurora
Use same font as used in my logo
or complimenting fonts
Modern
Marlene Oduya
Spray Technician
4072 Amber Willow Lane
Suite C
Chesapeake, Virginia 23487
auroramist@fernpost.example
In the logos provided, I included a Bramwick logo which is the product I use. Would like to somehow make that work on the card but not large. Would like to see fonts that compliment the logo but not the same necessarily

```html
<!DOCTYPE html>
<html lang="en">
<head>
<meta charset="utf-8">
<title>Mist Aurora — Business Card</title>
<link href="https://fonts.googleapis.com/css2?family=Montserrat:wght@700&family=Open+Sans:wght@400;600&display=swap" rel="stylesheet">
<style>
  :root {
    --backdrop: #e4e2df;
    --bronze: #7b4431;
    --bronze-dark: #6a3a29;
    --paper: #ffffff;
    --ink: #4a4a4a;
    --soft-grey: #9a9a9a;
    --pale-grey: #cfcfcf;
    --logo-light: #ffffff;
  }
  * { box-sizing: border-box; margin: 0; padding: 0; }
  html, body { width: 1200px; height: 864px; overflow: hidden; }
  body {
    background: var(--backdrop);
    font-family: "Open Sans", Arial, sans-serif;
    position: relative;
  }
  .card {
    position: absolute;
    top: 278px;
    width: 540px;
    height: 309px;
    border-radius: 18px;
    overflow: hidden;
    box-shadow: 0 6px 18px rgba(0,0,0,.18);
  }
  .card-front { left: 40px; background: var(--bronze); }
  .card-back { left: 620px; background: var(--paper); }

  .brand { position: absolute; }
  .brand-row { display: flex; align-items: center; gap: 10px; }
  .brand-dot { width: 14px; height: 14px; border-radius: 50%; }
  .brand-name {
    font-family: "Montserrat", Arial, sans-serif;
    font-weight: 700;
    letter-spacing: -0.5px;
    line-height: 1;
  }
  .brand-tagline {
    font-size: 13px;
    letter-spacing: 0.6px;
    margin-top: 4px;
    margin-left: 24px;
  }

  .card-front .brand { left: 50%; top: 50%; transform: translate(-50%, -50%); }
  .card-front .brand-dot { background: var(--logo-light); }
  .card-front .brand-name { font-size: 40px; color: var(--logo-light); }
  .card-front .brand-tagline { color: var(--logo-light); }

  .back-art { position: absolute; inset: 0; }

  .holder {
    position: absolute;
    right: 30px;
    top: 118px;
    text-align: right;
  }
  .holder-name { font-size: 17px; font-weight: 600; color: var(--bronze); }
  .holder-role { font-size: 12px; color: var(--ink); margin-top: 2px; }

  .card-back .brand { left: 30px; top: 168px; }
  .card-back .brand-dot { background: var(--bronze); }
  .card-back .brand-name { font-size: 30px; color: var(--bronze); }
  .card-back .brand-tagline { font-size: 11px; color: var(--ink); margin-left: 24px; }

  .contact {
    position: absolute;
    left: 30px;
    top: 226px;
    list-style: none;
  }
  .contact li {
    display: flex;
    align-items: center;
    gap: 8px;
    font-size: 11px;
    line-height: 17px;
    color: var(--ink);
  }
  .contact-icon {
    width: 12px; height: 12px; border-radius: 50%;
    background: var(--bronze);
    display: flex; align-items: center; justify-content: center;
    flex: none;
  }
  .contact-icon svg { width: 8px; height: 8px; }
  .contact-spacer { width: 12px; flex: none; }
</style>
</head>
<body>
  <section class="card card-front" aria-label="Card front">
    <div class="brand">
      <div class="brand-row">
        <span class="brand-dot"></span>
        <span class="brand-name">MistAurora</span>
      </div>
      <div class="brand-tagline">mobile spray tan service</div>
    </div>
  </section>

  <section class="card card-back" aria-label="Card back">
    <svg class="back-art" viewBox="0 0 540 309" preserveAspectRatio="none" aria-hidden="true">
      <path d="M0 0 H540 V30 C390 48 170 105 0 175 Z" fill="var(--bronze)"/>
      <path d="M0 188 C170 118 390 62 540 46" fill="none" stroke="var(--soft-grey)" stroke-width="6"/>
      <path d="M0 200 C170 132 390 76 540 60" fill="none" stroke="var(--pale-grey)" stroke-width="3"/>
    </svg>

    <div class="holder">
      <div class="holder-name">Marlene Oduya</div>
      <div class="holder-role">Spray Technician</div>
    </div>

    <div class="brand">
      <div class="brand-row">
        <span class="brand-dot"></span>
        <span class="brand-name">MistAurora</span>
      </div>
      <div class="brand-tagline">mobile spray tan service</div>
    </div>

    <ul class="contact">
      <li>
        <span class="contact-icon"><svg viewBox="0 0 10 10"><path d="M5 1 a3 3 0 0 1 3 3 c0 2-3 5-3 5 s-3-3-3-5 a3 3 0 0 1 3-3z" fill="#fff"/></svg></span>
        4072 Amber Willow Lane, Suite C
      </li>
      <li><span class="contact-spacer"></span>Chesapeake, Virginia 23487</li>
      <li>
        <span class="contact-icon"><svg viewBox="0 0 10 10"><path d="M2 1 h2 l1 2 -1 1 c.5 1 1 1.5 2 2 l1-1 2 1 v2 c-4 0-7-3-7-7z" fill="#fff"/></svg></span>
        757.555.0148
      </li>
      <li>
        <span class="contact-icon"><svg viewBox="0 0 10 10"><rect x="1.5" y="2.5" width="7" height="5" fill="none" stroke="#fff" stroke-width="1"/><path d="M1.5 2.5 L5 5.5 L8.5 2.5" fill="none" stroke="#fff" stroke-width="1"/></svg></span>
        auroramist@fernpost.example
      </li>
    </ul>
  </section>
</body>
</html>
```